Geschäftspapiere für Lasergravuren
Zielgruppe
Lasergravuren z.B. auf Glas, Holz, Filz, Papier, Acryl, eloxierten Aluminium zu Dekorationszwecken,
Ausschneiden von Elementen z.B. aus Holz, Filz, Papier, Acryl usw. zu Dekorationszwecken mit dem Lasergravierer.
Anfertigung verschiedener Dekorationsartikel,
Zielgruppe: Frauen (mit Familien) aller Altersgruppen, die Freude am Dekorieren und Verschenken haben
Aufgabenstellung
Das vorhandene Logo soll mit eingebunden werden

```html
<!DOCTYPE html>
<html lang="de">
<head>
<meta charset="utf-8">
<title>Lumenora – Briefbogen</title>
<link rel="stylesheet" href="https://fonts.googleapis.com/css2?family=Open+Sans:wght@300;400&family=Arimo:wght@400&display=swap">
<style>
  :root {
    --paper: #ffffff;
    --gold: #b0843f;
    --grey: #6f6f6f;
    --text: #5a5a5a;
    --line-light: #c9c9c9;
  }
  * { margin: 0; padding: 0; box-sizing: border-box; }
  html, body { width: 866px; height: 1200px; overflow: hidden; background: var(--paper); }
  .letterhead { position: relative; width: 866px; height: 1200px; background: var(--paper); font-family: "Open Sans", Arial, sans-serif; color: var(--text); }

  .brand { position: absolute; top: 20px; left: 0; width: 830px; text-align: center; }
  .brand-circle { display: block; width: 64px; height: 64px; margin: 0 auto; border: 1.5px solid var(--gold); border-radius: 50%; }
  .brand-name { display: block; margin-top: 6px; font-family: "Open Sans", Arial, sans-serif; font-weight: 300; font-size: 54px; letter-spacing: 1px; color: var(--grey); line-height: 1.1; }

  .sender-line { position: absolute; top: 214px; left: 92px; font-family: "Arimo", Arial, sans-serif; font-size: 10px; color: var(--text); padding-bottom: 2px; border-bottom: 1px solid var(--line-light); }
  .sender-line .divider { color: var(--gold); padding: 0 2px; }

  .fold-mark { position: absolute; left: 0; width: 31px; height: 1px; background: var(--gold); }
  .fold-mark.upper { top: 421px; }
  .fold-mark.lower { top: 824px; }

  .side-band { position: absolute; top: 0; right: 0; width: 36px; height: 1200px; background: var(--gold); }
  .side-band::before { content: ""; position: absolute; top: 0; left: 18px; width: 2px; height: 100%; background: var(--paper); opacity: .7; }

  .footer-band { position: absolute; top: 1113px; left: 0; width: 775px; height: 22px; background: var(--grey); }
  .footer-ornament { position: absolute; top: 1085px; left: 770px; width: 60px; height: 76px; background: radial-gradient(circle at 45% 50%, var(--grey) 0 30%, rgba(176,132,63,.55) 31%, rgba(255,255,255,0) 70%); }

  .contact { position: absolute; top: 1150px; font-size: 14px; line-height: 20px; color: var(--text); }
  .contact.address { left: 216px; }
  .contact.phone { left: 381px; }
  .contact.web { left: 542px; }
  .contact-row { display: flex; align-items: center; gap: 6px; }
  .contact-row svg { width: 12px; height: 12px; fill: var(--gold); flex: none; }
</style>
</head>
<body>
<div class="letterhead">
  <header class="brand">
    <span class="brand-circle"></span>
    <span class="brand-name">Lumenora</span>
  </header>

  <p class="sender-line">Lindenweg 12 <span class="divider">|</span> 30451 Musterstadt</p>

  <span class="fold-mark upper"></span>
  <span class="fold-mark lower"></span>

  <div class="side-band"></div>

  <div class="footer-band"></div>
  <div class="footer-ornament" role="img" aria-label="Illustration eines Lasergravurkopfs mit goldenen Lichtstrahlen"></div>

  <footer>
    <div class="contact address">
      <p>Ahornallee 8</p>
      <p>31135 Beispielstadt</p>
    </div>
    <div class="contact phone">
      <p class="contact-row">
        <svg viewBox="0 0 12 12" aria-hidden="true"><path d="M2.5 1 L4.5 1 L5.2 3.6 L4 4.6 C4.7 6 5.9 7.3 7.4 8 L8.4 6.8 L11 7.5 L11 9.5 C11 10.3 10.3 11 9.5 11 C5 11 1 7 1 2.5 C1 1.7 1.7 1 2.5 1 Z"/></svg>
        040 / 000 00 318
      </p>
      <p class="contact-row">
        <svg viewBox="0 0 12 12" aria-hidden="true"><path d="M3 1h6v3H3z M1 4.5h10v5H9V8H3v1.5H1z M3.5 8.5h5V11h-5z"/></svg>
        040 / 000 00 318
      </p>
    </div>
    <div class="contact web">
      <p class="contact-row">
        <svg viewBox="0 0 12 12" aria-hidden="true"><path d="M6 1a5 5 0 1 0 0 10A5 5 0 0 0 6 1zm0 1.2c.6.6 1.1 1.7 1.3 3.2H4.7C4.9 3.9 5.4 2.8 6 2.2zM2.2 6.6h1.5c.1 1.2.4 2.2.8 2.9A3.9 3.9 0 0 1 2.2 6.6zm0-1.2a3.9 3.9 0 0 1 2.3-2.9c-.4.7-.7 1.7-.8 2.9zm3.8 4.4c-.6-.6-1.1-1.7-1.3-3.2h2.6c-.2 1.5-.7 2.6-1.3 3.2zm1.5-.3c.4-.7.7-1.7.8-2.9h1.5a3.9 3.9 0 0 1-2.3 2.9zm.8-4.1c-.1-1.2-.4-2.2-.8-2.9a3.9 3.9 0 0 1 2.3 2.9z"/></svg>
        www.lumenora-deko.de
      </p>
      <p class="contact-row">
        <svg viewBox="0 0 12 12" aria-hidden="true"><path d="M1 3h10v7H1z M1 3l5 4 5-4" stroke="#fff" stroke-width=".8"/></svg>
        post@lumenora-deko.de
      </p>
    </div>
  </footer>
</div>
</body>
</html>
```